Community Youth Organisation needs a flyer template design for youth workshop

We require a flyer design that can be used for ongoing youth workshops targetted at young people 11-19 with intellectual disabilities (including Autism and Aspergers). We are hoping the flyer can be used over and over again when advertising our upcoming youth workshop series. Each workshop series will be approx 5 weeks and will be based on a particular topic. For example, our first workshop series will be run every Monday afternoon for 5 weeks on the topic "Conflict and Anger Management" (see attached info). We will then run a different workshop series on a different topic so we would like the same design to be used however with the possibility of editing the specific workshop info on it (e.g. dates, topic). We would require our BRVA logo on the flyer and graphics that would grab the attention of young people aged 11-19 with intellectual disabilities.

Target Market(s)

young people aged 11-19 with intellectual disabilities and their parents/carers

Industry/Entity Type

Advertising

Requirements
Must have
• BRVA Logo as prominent
Information as provided in attachment however in any "look" you feel would be appealing to the target group

```html
<!DOCTYPE html>
<html lang="en">
<head>
<meta charset="utf-8">
<title>Youth Workshops – BRVA</title>
<link href="https://fonts.googleapis.com/css2?family=Amatic+SC:wght@700&family=Nunito:wght@400;600;700;800&display=swap" rel="stylesheet">
<style>
  :root {
    --sky-top: #2f6fae;
    --sky-mid: #5a97cf;
    --sky-low: #a9cdea;
    --navy: #1d4f86;
    --ink: #173a66;
    --orange: #ea6a22;
    --yellow: #ffe11a;
    --white: #ffffff;
    --grass: #7fb241;
    --grass-dark: #4f8a2c;
  }
  * { box-sizing: border-box; margin: 0; padding: 0; }
  html, body { width: 849px; height: 1200px; overflow: hidden; }
  body { font-family: "Nunito", Arial, sans-serif; color: var(--ink); }

  .flyer {
    position: relative;
    width: 849px; height: 1200px; overflow: hidden;
    background: linear-gradient(180deg, var(--sky-top) 0%, var(--sky-mid) 25%, var(--sky-low) 55%, #d9ebf7 75%);
  }

  .kids-top {
    position: absolute; left: 0; top: 0; width: 160px; height: 370px;
    background: radial-gradient(ellipse at 45% 45%, #f2a55a 0%, #e07a3a 35%, rgba(90,150,210,0) 72%);
  }

  .title {
    position: absolute; left: 160px; top: 14px; width: 660px; height: 140px;
    overflow: hidden; white-space: nowrap;
    font-family: "Amatic SC", "Comic Sans MS", cursive;
    font-weight: 700; font-size: 116px; line-height: 140px; letter-spacing: 1px;
    text-shadow: 0 3px 6px rgba(0,0,0,.15);
  }
  .title .youth { color: var(--white); }
  .title .workshops { color: var(--yellow); }

  .dotted-rule {
    position: absolute; left: 160px; top: 160px; width: 652px;
    border-top: 4px dotted var(--white);
  }

  .intro {
    position: absolute; left: 155px; top: 190px; width: 665px;
    font-size: 16px; line-height: 1.42; color: var(--white);
  }
  .intro p + p { margin-top: 10px; }
  .intro strong { font-weight: 800; }

  .panel {
    position: absolute; left: 28px; top: 366px; width: 794px; height: 560px;
    border-radius: 28px 28px 0 0;
    background: linear-gradient(180deg, rgba(255,255,255,.97) 0%, rgba(255,255,255,.93) 65%, rgba(255,255,255,0) 100%);
  }

  .workshop-title {
    position: absolute; left: 0; top: 386px; width: 849px; text-align: center;
    font-size: 23px; color: var(--orange); font-weight: 400;
  }
  .workshop-title strong { font-weight: 800; }

  .workshop-desc {
    position: absolute; left: 55px; top: 425px; width: 739px; text-align: center;
    font-size: 16.6px; line-height: 1.42; color: #2a5b94;
  }

  .schedule {
    position: absolute; left: 47px; top: 512px; width: 754px;
    border-collapse: collapse; font-size: 14.5px; color: var(--navy);
  }
  .schedule th {
    background: var(--navy); color: var(--white); height: 37px;
    font-weight: 800; font-size: 16px; border: 1.5px solid var(--navy);
  }
  .schedule td {
    border: 1.5px solid var(--navy); height: 32.4px; background: rgba(255,255,255,.85);
  }
  .schedule .date { padding-left: 20px; width: 251px; }
  .schedule .time, .schedule .location { text-align: center; vertical-align: middle; line-height: 1.45; }
  .schedule .time { width: 251px; }
  .location-brand { display: inline-flex; align-items: center; gap: 6px; margin-top: 8px; font-weight: 800; font-size: 22px; color: var(--navy); }
  .location-brand .dot { width: 12px; height: 12px; border-radius: 50%; background: var(--orange); }

  .register {
    position: absolute; left: 0; top: 733px; width: 849px; text-align: center; color: var(--navy);
  }
  .register h2 { font-size: 20px; font-weight: 800; margin-bottom: 6px; }
  .register .line { font-size: 15.5px; line-height: 1.6; }
  .register .big { font-size: 25px; font-weight: 800; color: var(--orange); vertical-align: -2px; }
  .register .note { font-size: 13.6px; line-height: 1.45; margin: 10px auto 0; width: 610px; }

  .scene-bottom {
    position: absolute; left: 0; top: 880px; width: 849px; height: 320px;
    background: linear-gradient(180deg, rgba(200,225,240,0) 0%, #b9d8a0 30%, var(--grass) 60%, var(--grass-dark) 100%);
  }

  .brand-badge {
    position: absolute; right: 0; bottom: 0; width: 195px; height: 100px;
    background: var(--white); border-radius: 26px 0 0 0;
    display: flex; align-items: center; justify-content: center; gap: 10px;
    font-size: 40px; font-weight: 800; color: var(--navy);
  }
  .brand-badge .dot { width: 20px; height: 20px; border-radius: 50%; background: var(--orange); }
</style>
</head>
<body>
<main class="flyer">
  <div class="kids-top" role="img" aria-label="Cartoon children jumping and waving"></div>

  <h1 class="title"><span class="youth">Youth</span> <span class="workshops">WORKSHOPS</span></h1>
  <div class="dotted-rule"></div>

  <section class="intro">
    <p>The <strong>BRVA Brookvale Community Youth Service Workshop Series</strong> caters for young people between the ages of 11 -19 years with intellectual disabilities as well as those with Autism Spectrum Disorder, Asperger’s and ADHD.</p>
    <p>Workshops provide young people with an opportunity to socialise with their peers while learning essential life skills. They include a combination of hands on activities, group work and discussion. All workshops include afternoon tea and are provided free of charge.</p>
  </section>

  <div class="scene-bottom" role="img" aria-label="Cartoon children playing on a green hill in front of a city skyline"></div>
  <div class="panel"></div>

  <h2 class="workshop-title">WORKSHOP 1:&nbsp; <strong>CONFLICT AND ANGER MANAGEMENT</strong></h2>
  <p class="workshop-desc">During the workshops participants will learn to identify the physical and emotional symptoms of anger, understand what their personal triggers are, learn techniques to express their emotions in a positive manner and discover appropriate ways to respond to bullying behaviours.</p>

  <table class="schedule">
    <thead>
      <tr><th>DATE</th><th>TIME</th><th>LOCATION</th></tr>
    </thead>
    <tbody>
      <tr>
        <td class="date">Monday 15 April 2013</td>
        <td class="time" rowspan="5">Every workshop is<br>3.15pm - 5.00pm</td>
        <td class="location" rowspan="5">BRVA<br>42 Wattle Lane<br>Brookvale QLD 4000<br><span class="location-brand"><span class="dot"></span>BRVA</span></td>
      </tr>
      <tr><td class="date">Monday 22 April 2013</td></tr>
      <tr><td class="date">Monday 29 April 2013</td></tr>
      <tr><td class="date">Monday 6 May 2013</td></tr>
      <tr><td class="date">Monday 13 May 2013</td></tr>
    </tbody>
  </table>

  <section class="register">
    <h2>HOW TO REGISTER:</h2>
    <p class="line">To register simply contact Jess Moreland, Youth and Family Worker</p>
    <p class="line">via phone <span class="big">3555 0142</span> or email <span class="big">bfc@brva.org.au</span></p>
    <p class="note">Please be aware that participants are served on a first come first served basis and that by registering for a workshop series participants are agreeing to attend all relevant sessions.</p>
  </section>

  <div class="brand-badge"><span class="dot"></span>BRVA</div>
</main>
</body>
</html>
```